Business Card for Graphic Design Firm

This project is for a new graphic design firm based in New Jersey called Velmoric. We outsource graphic design and marketing jobs. We want to communicate that this is a professional company but it as well creative and artistic. This card may be used as a horizontal double sided paper card or a vertical single sided translucent card so feel free to submit designs in whichever format or both.
Updates

Reason: Extending the deadline because I'm not exactly satisfied with the designs so far.

Please view the updated project brief

Target Market(s)

Adults aged 25-60

Industry/Entity Type

Graphic Design

Font styles to use
Serif
Sans Serif

Requirements
Nice to have
• Maybe a triangular pattern around the edges similar to our logo

```html
<!DOCTYPE html>
<html lang="en">
<head>
<meta charset="utf-8">
<title>Velmoric Business Card</title>
<link href="https://fonts.googleapis.com/css2?family=Open+Sans:wght@400;600;700&display=swap" rel="stylesheet">
<style>
  :root {
    --backdrop: #2b2b2d;
    --card-orange: #f5821f;
    --card-grey: #6c757a;
    --ink-white: #ffffff;
    --ink-gold: #f3b321;
    --ink-dark: #5a5f63;
  }
  * { margin: 0; padding: 0; box-sizing: border-box; }
  html, body {
    width: 1200px; height: 800px; overflow: hidden;
    background: var(--backdrop);
    font-family: "Open Sans", Arial, sans-serif;
  }
  .canvas {
    position: relative; width: 1200px; height: 800px;
    display: flex; align-items: center; justify-content: center; gap: 60px;
  }
  .card {
    position: relative; width: 510px; height: 300px;
    border-radius: 4px; overflow: hidden;
  }
  .card--front {
    background: var(--card-orange);
    display: flex; align-items: center; justify-content: center; gap: 18px;
  }
  .brand { display: flex; align-items: center; gap: 14px; }
  .brand__mark { width: 34px; height: 34px; background: var(--ink-white); }
  .brand__name {
    font-weight: 600; font-size: 52px; letter-spacing: 4px;
    color: var(--ink-white); text-transform: uppercase;
  }
  .card--back { background: var(--card-grey); }
  .card--back .brand {
    position: absolute; left: 34px; bottom: 44px; gap: 10px;
  }
  .card--back .brand__mark { width: 20px; height: 20px; }
  .card--back .brand__name { font-size: 28px; letter-spacing: 2px; }
  .contact {
    position: absolute; right: 32px; top: 48px; text-align: right;
  }
  .contact__name { font-weight: 700; font-size: 17px; color: var(--ink-white); }
  .contact__role { font-size: 12px; color: var(--ink-gold); margin-bottom: 14px; }
  .contact__row {
    display: flex; justify-content: flex-end; align-items: center; gap: 10px;
    font-size: 12.5px; color: var(--ink-gold); margin-bottom: 10px; line-height: 1.35;
  }
  .contact__icon { width: 22px; height: 22px; flex: none; }
</style>
</head>
<body>
<main class="canvas">
  <section class="card card--front" aria-label="Card front">
    <div class="brand">
      <span class="brand__mark"></span>
      <span class="brand__name">Velmoric</span>
    </div>
  </section>

  <section class="card card--back" aria-label="Card back">
    <div class="contact">
      <p class="contact__name">Daniel Hollis</p>
      <p class="contact__role">Hybrid Clouds</p>
      <div class="contact__row">
        <span>+1 201 555 0148</span>
        <svg class="contact__icon" viewBox="0 0 22 22" aria-hidden="true">
          <circle cx="11" cy="11" r="10" fill="none" stroke="#fff" stroke-width="1.2"/>
          <path d="M7.5 6.5l2 0 1 2.5-1.2 1a6 6 0 0 0 2.7 2.7l1-1.2 2.5 1 0 2a1 1 0 0 1-1 1A8 8 0 0 1 6.5 7.5a1 1 0 0 1 1-1z" fill="#f3b321"/>
        </svg>
      </div>
      <div class="contact__row">
        <span>daniel@velmoric.com</span>
        <svg class="contact__icon" viewBox="0 0 22 22" aria-hidden="true">
          <circle cx="11" cy="11" r="10" fill="none" stroke="#fff" stroke-width="1.2"/>
          <rect x="6" y="7.5" width="10" height="7" fill="#f3b321"/>
          <path d="M6 7.5l5 4 5-4" fill="none" stroke="#6c757a" stroke-width="1"/>
        </svg>
      </div>
      <div class="contact__row">
        <span>218 Orchard Lane, Montclair<br>NJ 07042, USA</span>
        <svg class="contact__icon" viewBox="0 0 22 22" aria-hidden="true">
          <circle cx="11" cy="11" r="10" fill="none" stroke="#fff" stroke-width="1.2"/>
          <path d="M11 5.5a3.8 3.8 0 0 1 3.8 3.8c0 2.8-3.8 7-3.8 7s-3.8-4.2-3.8-7A3.8 3.8 0 0 1 11 5.5z" fill="#f3b321"/>
          <circle cx="11" cy="9.3" r="1.4" fill="#6c757a"/>
        </svg>
      </div>
    </div>
    <div class="brand">
      <span class="brand__mark"></span>
      <span class="brand__name">Velmoric</span>
    </div>
  </section>
</main>
</body>
</html>
```